Taste of Kerwin digital board & Corflute design

Hi, we are a restaurant based in Parramatta (NSW). We are looking forward for a creative design for our menu to attract the customers at our two different locations.
1. We need a 80 x 296 cm digital board design for display of menu items.
few of the drafts are attached to provide a reference. However, we would request not the similar ones but certain novel and creative designs.
2. We need 3 different 900x1200mm 'A-Frame' or Corflute designs to
-- display our opening hours and details
-- display our flagship items of chaat counter(lassa thali)
--display our menu for TOK, Brindlemarts
--display our menu for TOK, Harrowgate.

```html
<!DOCTYPE html>
<html lang="en">
<head>
<meta charset="utf-8">
<title>Taste of Kerwin — Our Menu</title>
<link rel="stylesheet" href="https://fonts.googleapis.com/css2?family=Alfa+Slab+One&family=Montserrat:ital,wght@0,600;0,700;0,800;1,700&display=swap">
<style>
  :root {
    --page-bg: #f2f2f2;
    --sun: #fdbf3a;
    --sun-soft: #f9c44a;
    --band: #e8e8e8;
    --paper: #ffffff;
    --ink: #1c1c1c;
    --orange: #f57f20;
    --pill: #fbe5a8;
    --deal-red: #e3171d;
    --title-red: #7a1a0c;
    --bar: #fbbd1e;
  }
  * { box-sizing: border-box; margin: 0; padding: 0; }
  html, body { width: 1200px; height: 1200px; overflow: hidden; background: var(--page-bg); }
  .poster {
    position: absolute; left: 150px; top: 0; width: 900px; height: 1200px;
    background: var(--paper); overflow: hidden;
    font-family: "Montserrat", sans-serif; color: var(--ink);
  }
  .hero { position: absolute; left: 0; top: 0; width: 900px; height: 432px;
    background: radial-gradient(circle at 40% 40%, #fcc84f, var(--sun) 70%); }
  .band { position: absolute; left: 0; top: 432px; width: 900px; height: 241px; background: var(--band); }
  .photo { position: absolute; }
  .dish { border-radius: 50%; box-shadow: 0 4px 10px rgba(0,0,0,.2); }
  .brand-box { position: absolute; left: 272px; top: 0; width: 355px; height: 168px; background: var(--paper);
    display: flex; align-items: center; justify-content: center; gap: 10px; }
  .brand-mark { width: 14px; height: 14px; background: var(--orange); }
  .brand-name { font-weight: 600; font-size: 34px; letter-spacing: -0.5px; color: var(--ink); }
  .dash { position: absolute; left: 224px; width: 450px; border-top: 3px dashed var(--paper); }
  .menu-title { position: absolute; left: 0; width: 900px; top: 220px; text-align: center;
    font-family: "Alfa Slab One", serif; font-size: 62px; letter-spacing: 3px; color: var(--ink);
    text-shadow: 2px 2px 0 #fff; }
  .card-frame { position: absolute; width: 309px; height: 147px; border: 3px solid var(--orange);
    box-shadow: 0 3px 6px rgba(0,0,0,.15); }
  .card-title { position: absolute; width: 309px; text-align: center; font-family: "Alfa Slab One", serif;
    font-size: 32px; letter-spacing: 1.5px; color: var(--ink); text-shadow: 2px 2px 0 #fff, -1px -1px 0 #fff; }
  .card-list { position: absolute; width: 233px; height: 83px; background: var(--paper);
    box-shadow: 0 4px 8px rgba(0,0,0,.2); display: flex; flex-direction: column; justify-content: center;
    align-items: center; font-weight: 800; font-size: 15px; letter-spacing: 1.8px; line-height: 22px; }
  .card-list .note { color: var(--orange); font-style: italic; font-weight: 700; letter-spacing: 1px; }
  .section-title { position: absolute; text-align: center; font-family: "Alfa Slab One", serif; font-size: 22px;
    color: var(--sun); letter-spacing: 1px;
    text-shadow: 1px 1px 0 var(--title-red), -1px -1px 0 var(--title-red), 1px -1px 0 var(--title-red), -1px 1px 0 var(--title-red), 2px 3px 2px rgba(0,0,0,.35); }
  .pill { position: absolute; width: 251px; height: 34px; border-radius: 17px; background: var(--pill);
    display: flex; align-items: center; justify-content: center; font-weight: 800; font-size: 19px; }
  .divider { position: absolute; left: 449px; top: 847px; width: 2px; height: 306px; background: var(--bar); }
  .deal-title { position: absolute; left: 134px; width: 251px; top: 1078px; text-align: center;
    font-family: "Alfa Slab One", serif; font-size: 28px; color: var(--deal-red); letter-spacing: 2px;
    text-shadow: 2px 2px 0 #fff, 2px 3px 3px rgba(0,0,0,.3); }
  .deal-item { position: absolute; left: 84px; width: 351px; top: 1123px; text-align: center;
    font-weight: 800; font-size: 19px; letter-spacing: .5px; }
  .footer-bar { position: absolute; left: 106px; top: 1183px; width: 688px; height: 17px; background: var(--bar); }
</style>
</head>
<body>
<main class="poster">
  <div class="hero"></div>
  <div class="band"></div>

  <div class="photo dish" role="img" aria-label="Bowl of ragda pattice with spoon" style="left:37px;top:-30px;width:188px;height:166px;background:radial-gradient(circle,#d6983c 30%,#f3efe6 55%,#fff 70%);"></div>
  <div class="photo dish" role="img" aria-label="Bowl of chopped red onion" style="left:-30px;top:213px;width:112px;height:130px;background:radial-gradient(circle,#d9a7c4 50%,#fff 62%);"></div>
  <div class="photo dish" role="img" aria-label="Green chutney bowl with boondi" style="left:694px;top:36px;width:116px;height:116px;background:radial-gradient(circle,#6f8a2a 55%,#3e5f1c 75%);"></div>
  <div class="photo dish" role="img" aria-label="Plate of dahi puri chaat" style="left:709px;top:148px;width:186px;height:186px;background:radial-gradient(circle,#c89a5a 45%,#f5f2ec 62%,#fff 72%);"></div>

  <header class="brand-box">
    <span class="brand-mark"></span>
    <span class="brand-name">Taste of Kerwin</span>
  </header>

  <div class="dash" style="top:201px"></div>
  <h1 class="menu-title">OUR MENU</h1>
  <div class="dash" style="top:303px"></div>

  <!-- Momos -->
  <div class="card-frame" role="img" aria-label="Steamed momos with red chutney" style="left:116px;top:354px;background:linear-gradient(135deg,#f1ebe0,#e8541f 50%,#efe5d4);"></div>
  <div class="card-title" style="left:116px;top:332px">MOMOS</div>
  <div class="card-list" style="left:154px;top:467px">
    <span>VEG MOMOS</span><span>CHICKEN MOMOS</span><span class="note">Steam of Fried</span>
  </div>

  <!-- Thali -->
  <div class="card-frame" role="img" aria-label="Indian thali platter with rice, curries and roti" style="left:476px;top:354px;background:linear-gradient(135deg,#f5f5f5,#c7a572 45%,#8e7a5a 70%,#f5f5f5);"></div>
  <div class="card-title" style="left:476px;top:332px">THALI</div>
  <div class="card-list" style="left:513px;top:467px">
    <span>VEG THALI</span><span>NON-VEGTHALI</span>
  </div>

  <!-- Biryani -->
  <div class="card-frame" role="img" aria-label="Bowl of vegetable biryani" style="left:116px;top:597px;background:linear-gradient(135deg,#f3f3f3,#e2c85a 45%,#d98a3c 60%,#f0ebe4);"></div>
  <div class="card-title" style="left:116px;top:575px">BIRYANI</div>
  <div class="card-list" style="left:154px;top:714px">
    <span>VEG BIRYANI</span><span>GOAT BIRYANI</span><span>CHICKEN BIRYANI</span>
  </div>

  <!-- Drinks -->
  <div class="card-frame" role="img" aria-label="Glass of mango lassi with mint" style="left:476px;top:597px;background:linear-gradient(135deg,#f7e2a6,#f7c94e 50%,#3f6a28 85%);"></div>
  <div class="card-title" style="left:476px;top:575px">DRINKS</div>
  <div class="card-list" style="left:513px;top:714px">
    <span>MANGO LASSI</span><span>MASALA CHAI</span>
  </div>

  <!-- Street food -->
  <h2 class="section-title" style="left:84px;width:351px;top:837px">INDIAN STREET FOOD</h2>
  <div class="pill" style="left:134px;top:880px">PANI PURI</div>
  <div class="pill" style="left:134px;top:926px">CHAAT PAPADI</div>
  <div class="pill" style="left:134px;top:972px">SAMOSA CHAAT</div>
  <div class="pill" style="left:134px;top:1018px">BHELPURI</div>

  <h2 class="deal-title">COMBO DEAL</h2>
  <p class="deal-item">SAMOSA WITH CHAI</p>

  <div class="divider"></div>

  <!-- Curries -->
  <h2 class="section-title" style="left:508px;width:251px;top:837px">CURRIES</h2>
  <div class="pill" style="left:508px;top:880px">CHICKEN CURRY</div>
  <div class="pill" style="left:508px;top:926px">LAMB CURRY</div>
  <div class="pill" style="left:508px;top:972px">GOAT CURRY</div>
  <div class="pill" style="left:508px;top:1018px">PANEER CURRY</div>
  <div class="pill" style="left:508px;top:1064px">VEGETARIAN CURRY</div>
  <div class="pill" style="left:508px;top:1109px">DAL</div>

  <div class="photo" role="img" aria-label="Golden fried samosas with greens" style="left:778px;top:899px;width:122px;height:229px;border-radius:60px 0 0 60px;background:radial-gradient(circle at 70% 50%,#e8a24a 40%,#f3c27a 60%,rgba(255,255,255,0) 75%);"></div>

  <div class="footer-bar"></div>
</main>
</body>
</html>
```